Business Card Design Project

Bold, modern, clean business card design needed. Prefer double sided with art logo on the back. Front of card with company name logo, no art.

Target Market(s)

Our consulting company supports local, state and federal law enforcement officers. Therefore the design should be clean and direct with no flash or arrogance to it.

Industry/Entity Type

Business

```html
<!DOCTYPE html>
<html lang="en">
<head>
<meta charset="utf-8">
<title>Ardenline Business Card</title>
<link rel="stylesheet" href="https://fonts.googleapis.com/css2?family=Michroma&display=swap">
<style>
  :root {
    --page: #ffffff;
    --card-center: #3b3b3b;
    --card-edge: #0e0e0e;
    --text-light: #e6e6e6;
    --text-muted: #cfcfcf;
    --accent: #8fd400;
    --accent-dark: #4f8a00;
    --silver-light: #f2f2f2;
    --silver-dark: #8a8a8a;
    --icon-ink: #1a1a1a;
  }
  * { margin: 0; padding: 0; box-sizing: border-box; }
  html, body {
    width: 1200px;
    height: 347px;
    overflow: hidden;
    background: var(--page);
  }
  .sheet {
    position: relative;
    width: 1200px;
    height: 347px;
    font-family: "Michroma", sans-serif;
  }
  .card {
    position: absolute;
    top: 0;
    width: 579px;
    height: 347px;
    overflow: hidden;
    background: radial-gradient(ellipse at 50% 42%, var(--card-center) 0%, #242424 45%, var(--card-edge) 100%);
  }
  .card--front { left: 0; }
  .card--back { left: 621px; }

  /* Brand mark */
  .brand {
    position: absolute;
    display: flex;
    flex-direction: column;
    align-items: center;
    color: var(--text-light);
  }
  .brand__dot {
    border-radius: 50%;
    background: var(--accent);
  }
  .brand__name {
    color: var(--text-light);
    font-weight: 400;
    letter-spacing: 0.06em;
    white-space: nowrap;
  }
  .card--front .brand {
    left: 60px;
    top: 128px;
    width: 210px;
  }
  .card--front .brand__dot { width: 62px; height: 62px; margin-bottom: 26px; }
  .card--front .brand__name { font-size: 22px; }

  .card--back .brand {
    left: 40px;
    top: 48px;
    width: 500px;
  }
  .card--back .brand__dot { width: 120px; height: 120px; margin-bottom: 40px; }
  .card--back .brand__name { font-size: 42px; }

  /* Contact block */
  .holder {
    position: absolute;
    right: 50px;
    top: 60px;
    font-size: 15px;
    letter-spacing: 0.14em;
    color: var(--text-light);
    white-space: nowrap;
  }
  .contacts {
    position: absolute;
    right: 52px;
    top: 107px;
    list-style: none;
  }
  .contact {
    display: flex;
    align-items: center;
    justify-content: flex-end;
    height: 33.5px;
    gap: 10px;
    font-size: 9.5px;
    letter-spacing: 0.16em;
    text-transform: uppercase;
    color: var(--text-muted);
    white-space: nowrap;
  }
  .contact__icon {
    width: 21px;
    height: 21px;
    flex: none;
  }
  .contact__icon circle { fill: var(--accent); }
  .contact__icon .glyph { fill: var(--icon-ink); }

  /* Back band */
  .band-rule {
    position: absolute;
    left: 0;
    top: 291px;
    width: 100%;
    height: 7px;
    background: linear-gradient(180deg, var(--silver-light), var(--silver-dark));
  }
  .band {
    position: absolute;
    left: 0;
    top: 298px;
    width: 100%;
    height: 49px;
    background: radial-gradient(ellipse at 50% 30%, #a6ef10 0%, var(--accent) 45%, var(--accent-dark) 100%);
  }
</style>
</head>
<body>
<main class="sheet">

  <section class="card card--front" aria-label="Card front">
    <div class="brand">
      <span class="brand__dot"></span>
      <span class="brand__name">ARDENLINE</span>
    </div>

    <p class="holder">Mark Ellison</p>

    <ul class="contacts">
      <li class="contact">
        <span>555 018 274</span>
        <svg class="contact__icon" viewBox="0 0 20 20" aria-hidden="true">
          <circle cx="10" cy="10" r="10"/>
          <path class="glyph" d="M6.2 4.8l2 2-1.1 1.4c.7 1.6 1.9 2.8 3.5 3.6l1.4-1.1 2 2-1.3 1.9c-3.9-.6-7.1-3.8-7.9-7.9z"/>
        </svg>
      </li>
      <li class="contact">
        <span>12 Harbor Lane</span>
        <svg class="contact__icon" viewBox="0 0 20 20" aria-hidden="true">
          <circle cx="10" cy="10" r="10"/>
          <path class="glyph" d="M10 4.5l5.5 5h-1.6v5H11.4v-3.2H8.6v3.2H6.1v-5H4.5z"/>
        </svg>
      </li>
      <li class="contact">
        <span>@ardenline</span>
        <svg class="contact__icon" viewBox="0 0 20 20" aria-hidden="true">
          <circle cx="10" cy="10" r="10"/>
        </svg>
      </li>
      <li class="contact">
        <span>ardenline/page</span>
        <svg class="contact__icon" viewBox="0 0 20 20" aria-hidden="true">
          <circle cx="10" cy="10" r="10"/>
        </svg>
      </li>
      <li class="contact">
        <span>hello@ardenline.com</span>
        <svg class="contact__icon" viewBox="0 0 20 20" aria-hidden="true">
          <circle cx="10" cy="10" r="10"/>
          <path class="glyph" d="M4.5 6.5h11v7h-11z M5.5 7.3v.4l4.5 3.2 4.5-3.2v-.4z" fill-rule="evenodd"/>
        </svg>
      </li>
      <li class="contact">
        <span>www.ardenline.com</span>
        <svg class="contact__icon" viewBox="0 0 20 20" aria-hidden="true">
          <circle cx="10" cy="10" r="10"/>
          <path class="glyph" d="M7 4.5v10l2.4-2.2 1.7 3.6 1.5-.7-1.7-3.5 3.3-.2z"/>
        </svg>
      </li>
    </ul>
  </section>

  <section class="card card--back" aria-label="Card back">
    <div class="brand">
      <span class="brand__dot"></span>
      <span class="brand__name">ARDENLINE</span>
    </div>
    <div class="band-rule"></div>
    <div class="band"></div>
  </section>

</main>
</body>
</html>
```